Business Card Re-design

We are looking for a fresh bold look for general office business cards. We are a staffing agency that staffs industrial, coal mining, and clerical jobs.
Tag Line: We match the RIGHT talent with the RIGHT roles.
Harlow Office: 2473 W. Tallow Creek Rd, Harlow, OH - 47308
p. 555.203.6180 f. 555.203.6195
Dunmore Office: 264 S. Birch Ln, Dunmore, OH - 47152
p. 555.319.2047 f. 555.203.6195
After-Hours/Urgent 24hr Support Line 555.203.6172 opt.1
www.bluelanternworkforce.example

```html
<!DOCTYPE html>
<html lang="en">
<head>
<meta charset="utf-8">
<title>Blue Lantern Workforce – Business Cards</title>
<link href="https://fonts.googleapis.com/css2?family=Roboto+Condensed:wght@400;700&display=swap" rel="stylesheet">
<style>
  :root {
    --page: #e8e5e1;
    --card: #2f2f30;
    --band: #3e9a35;
    --brand: #2d5fa8;
    --accent: #3e9a35;
    --text-light: #ffffff;
    --text-dark: #262626;
  }
  * { margin: 0; padding: 0; box-sizing: border-box; }
  html, body {
    width: 1200px;
    height: 1047px;
    overflow: hidden;
    background: var(--page);
    font-family: "Roboto Condensed", "Arial Narrow", sans-serif;
  }
  .card {
    position: absolute;
    left: 220px;
    width: 759px;
    height: 446px;
    background: var(--card);
  }
  .card--front { top: 66px; }
  .card--back { top: 535px; }

  .brand {
    position: absolute;
    display: flex;
    align-items: center;
    color: var(--brand);
    font-weight: 700;
    text-transform: uppercase;
    line-height: 0.95;
  }
  .brand__mark { background: var(--accent); flex: none; }
  .brand--large { left: 150px; top: 122px; gap: 26px; font-size: 64px; letter-spacing: 1px; }
  .brand--large .brand__mark { width: 120px; height: 120px; }
  .brand--small { right: 36px; top: 40px; gap: 14px; font-size: 32px; letter-spacing: 0.5px; }
  .brand--small .brand__mark { width: 60px; height: 60px; }

  .band {
    position: absolute;
    left: 0;
    width: 100%;
    background: var(--band);
    display: flex;
    align-items: center;
    justify-content: center;
    white-space: nowrap;
  }
  .tagline {
    top: 359px;
    height: 47px;
    color: var(--text-light);
    font-size: 30px;
    font-weight: 400;
  }
  .hotline {
    top: 362px;
    height: 35px;
    color: var(--text-dark);
    font-size: 27px;
    font-weight: 700;
  }

  .offices {
    position: absolute;
    left: 53px;
    top: 156px;
    color: var(--text-light);
    font-size: 21px;
    line-height: 29px;
  }
  .office + .office { margin-top: 27px; }

  .website {
    position: absolute;
    left: 0;
    width: 100%;
    top: 408px;
    text-align: center;
    color: var(--text-light);
    font-size: 21px;
  }
</style>
</head>
<body>
  <section class="card card--front">
    <div class="brand brand--large">
      <span class="brand__mark"></span>
      <span class="brand__name">Blue Lantern<br>Workforce</span>
    </div>
    <p class="band tagline">We match the RIGHT talent with the RIGHT roles</p>
  </section>

  <section class="card card--back">
    <div class="brand brand--small">
      <span class="brand__mark"></span>
      <span class="brand__name">Blue Lantern<br>Workforce</span>
    </div>
    <div class="offices">
      <div class="office">
        <p>Harlow Office :</p>
        <p>2473 W. Tallow Creek Rd, Harlow, OH - 47308</p>
        <p>P. 555.203.6180 F. 555.203.6195</p>
      </div>
      <div class="office">
        <p>Dunmore Office:</p>
        <p>264 S. Birch Ln, Dunmore, OH - 47152</p>
        <p>P. 555.319.2047 F. 555.203.6195</p>
      </div>
    </div>
    <p class="band hotline">After-Hours/Urgent 24hr Support Line 555.203.6172 opt.1</p>
    <p class="website">www.bluelanternworkforce.example</p>
  </section>
</body>
</html>
```